・電子書籍の表紙デザインをお願いします。

・本の内容
モヤモヤグルグルしてるただの主婦でも、天職につながれば稼げるようになる。
自分の事を理解し天職につながることによって、
自信や人間関係やお金、仕事や健康までも、うまく回り始める。
私のエピソードから天職につながるプロセスを見てもらって解説してます。
後半で、あなたの天職につながるワークを実践して
スモールステップを踏み出せるようになるという内容になっています。

・デザイン要望
文字を大きく、パッと見て何が書いてあるかわかりやすいようにして欲しいです。

その他何かありましたら、気軽に質問して下さいね。
よろしくお願いいたします。

タイトルとして

スル~っととんとん拍子に
『ひらめく毎日!をひらく本』
モヤモヤグルグルしてたただの主婦の私が、
まさかの経営者になった理由
森川遥香

読者限定プレゼント
「何かしたい」でも「何をしたいのかわからない」
そんなあなたに
「星読みカルテ」プレゼント

入れて欲しいです。
とんとん拍子 → トントン拍子

軽快なイメージに一番近かったです。

皆さんのご提案、すべて素敵で迷いました。
ありがとうございました。

```html
<!DOCTYPE html>
<html lang="ja">
<head>
<meta charset="utf-8">
<title>ひらめく毎日!をひらく本</title>
<link href="https://fonts.googleapis.com/css2?family=M+PLUS+Rounded+1c:wght@500;700;800;900&display=swap" rel="stylesheet">
<style>
  :root {
    --pink: #ef5b8c;
    --pink-soft: #f9c6d6;
    --yellow: #ffd92e;
    --ink: #3a2a2a;
    --white: #ffffff;
  }
  * { margin: 0; padding: 0; box-sizing: border-box; }
  html, body { width: 750px; height: 1200px; overflow: hidden; background: var(--white); }
  .cover {
    position: relative; width: 750px; height: 1200px; overflow: hidden;
    background: var(--white);
    font-family: "M PLUS Rounded 1c", sans-serif; color: var(--ink);
  }

  /* vertical columns built from stacked glyph cells */
  .col { position: absolute; display: flex; flex-direction: column; align-items: center; width: 1em; }
  .col > span { display: block; width: 1em; height: 1.05em; line-height: 1.05em; text-align: center; }
  .col > span.r { transform: rotate(90deg); }

  .art { position: absolute; border-radius: 40px; }
  .art-flying { left: 95px; top: 30px; width: 118px; height: 280px;
    background: radial-gradient(ellipse at 50% 45%, var(--pink-soft), #fdeef3 65%, transparent 72%); }
  .art-cheer { left: 598px; top: 560px; width: 145px; height: 310px;
    background: radial-gradient(ellipse at 50% 50%, #fde4c8, #e9f4fa 65%, transparent 72%); }

  .bubble { position: absolute; left: 215px; top: 25px; width: 155px; height: 480px; }
  .bubble-line { font-size: 48px; font-weight: 800; top: 75px; }
  .bubble-line.first { left: 301px; }
  .bubble-line.second { left: 238px; }

  .author { left: 38px; top: 50px; font-size: 64px; font-weight: 800; }

  .title { font-weight: 900; paint-order: stroke fill; -webkit-text-stroke: 9px var(--ink); }
  .title-a { left: 346px; top: 30px; font-size: 108px; color: var(--pink); }
  .title-b { left: 450px; top: 420px; font-size: 140px; color: var(--yellow); }
  .title-c { left: 247px; top: 540px; font-size: 66px; font-weight: 800; color: var(--ink); }

  .gift-label { font-size: 24px; font-weight: 800; color: var(--pink); top: 335px; }
  .gift-label.first { left: 182px; }
  .gift-label.second { left: 152px; }
  .gift-box { position: absolute; left: 126px; top: 495px; width: 86px; height: 480px;
    border-left: 4px solid var(--pink); border-right: 4px solid var(--pink); }
  .gift-text { font-size: 19px; font-weight: 700; top: 505px; }
  .gift-text.first { left: 173px; }
  .gift-text.second { left: 143px; }
  .gift-text .hl { color: var(--pink); }

  .band { position: absolute; left: 0; top: 985px; width: 750px; height: 215px; background: var(--pink-soft); }
  .story-card { position: absolute; left: 220px; top: 890px; width: 528px; height: 298px; }
  .surprise { position: absolute; left: 14px; top: 1090px; font-size: 36px; font-weight: 800; color: var(--pink); transform: rotate(-8deg); }
  .story { position: absolute; left: 246px; top: 925px; width: 490px; font-weight: 800; line-height: 1.55; }
  .story .line-1 { font-size: 36px; display: block; }
  .story .line-2 { font-size: 46px; display: block; }
  .story .line-3 { font-size: 46px; display: block; }
  .story .accent { color: var(--pink); font-size: 56px; }
</style>
</head>
<body>
<main class="cover">
  <div class="art art-flying" role="img" aria-label="空を飛ぶ女性のイラスト"></div>
  <div class="art art-cheer" role="img" aria-label="喜ぶ女性のイラスト"></div>

  <svg class="bubble" viewBox="0 0 155 480" aria-hidden="true">
    <path d="M77 4 C132 4 151 80 151 230 C151 360 138 430 100 446 L124 476 L76 452 C30 448 4 380 4 230 C4 80 22 4 77 4 Z"
          fill="#ffffff" stroke="#3a2a2a" stroke-width="4"/>
  </svg>
  <p class="col bubble-line first"><span>ス</span><span>ル</span><span class="r">〜</span><span>っ</span><span>と</span></p>
  <p class="col bubble-line second"><span>ト</span><span>ン</span><span>ト</span><span>ン</span><span>拍</span><span>子</span><span>に</span></p>

  <p class="col author"><span>森</span><span>川</span><span>遥</span><span>香</span></p>

  <h1>
    <span class="col title title-a"><span>ひ</span><span>ら</span><span>め</span><span>く</span></span>
    <span class="col title title-b"><span>毎</span><span>日</span><span>！</span></span>
    <span class="col title-c"><span>を</span><span>ひ</span><span>ら</span><span>く</span><span>本</span></span>
  </h1>

  <p class="col gift-label first"><span>読</span><span>者</span><span>限</span><span>定</span></p>
  <p class="col gift-label second"><span>プ</span><span>レ</span><span>ゼ</span><span>ン</span><span>ト</span></p>
  <div class="gift-box"></div>
  <p class="col gift-text first"><span class="r">「</span><span>何</span><span>か</span><span>し</span><span>た</span><span>い</span><span class="r">」</span><span>で</span><span>も</span><span class="r">「</span><span>何</span><span>を</span><span>し</span><span>た</span><span>い</span><span>の</span><span>か</span><span>わ</span><span>か</span><span>ら</span><span>な</span><span>い</span><span class="r">」</span></p>
  <p class="col gift-text second"><span>そ</span><span>ん</span><span>な</span><span>あ</span><span>な</span><span>た</span><span>に</span><span class="r hl">「</span><span class="hl">星</span><span class="hl">読</span><span class="hl">み</span><span class="hl">カ</span><span class="hl">ル</span><span class="hl">テ</span><span class="r hl">」</span><span>プ</span><span>レ</span><span>ゼ</span><span>ン</span><span>ト</span><span>！</span></p>

  <div class="band"></div>
  <svg class="story-card" viewBox="0 0 528 298" aria-hidden="true">
    <path d="M14 14 L524 0 L512 296 L0 284 Z" fill="#ffffff" stroke="#ef5b8c" stroke-width="3"/>
  </svg>
  <p class="surprise">まさかの</p>
  <p class="story"><span class="line-1">グルグル モヤモヤしてた</span><span class="line-2">ただの主婦の私が、</span><span class="line-3"><span class="accent">経営者</span>になった理由</span></p>
</main>
</body>
</html>
```